Security Warning Sign

We have an existing sign that needs an update. I have attached a picture of the current square sign. We need to maintain the same wording. It needs to be professional and appropriate to attach to our customers fence. Also attached is a copy of our building sign which may lend some inspiration and hopefully the ai format will assist. The final sign will be 600mm x 600mmOur website is www.halvorngate.com.au

```html
<!DOCTYPE html>
<html lang="en">
<head>
<meta charset="utf-8">
<title>Security Warning Sign</title>
<link href="https://fonts.googleapis.com/css2?family=Roboto+Condensed:wght@700;800;900&family=Saira+Stencil+One&display=swap" rel="stylesheet">
<style>
  :root {
    --sign-orange: #ef8a1f;
    --sign-black: #151515;
    --sign-white: #ffffff;
  }
  html, body {
    margin: 0;
    padding: 0;
    width: 1200px;
    height: 1200px;
    overflow: hidden;
    background: var(--sign-white);
  }
  .sign {
    position: relative;
    width: 1200px;
    height: 1200px;
    overflow: hidden;
    background: var(--sign-orange);
    font-family: "Roboto Condensed", "Arial Narrow", sans-serif;
  }
  .mount-hole {
    position: absolute;
    width: 30px;
    height: 30px;
    border-radius: 50%;
    background: var(--sign-white);
  }
  .mount-hole.tl { left: 8px; top: 18px; }
  .mount-hole.tr { right: 8px; top: 18px; }
  .mount-hole.bl { left: 8px; bottom: 18px; }
  .mount-hole.br { right: 8px; bottom: 18px; }
  .sign-face {
    position: absolute;
    left: 58px;
    top: 58px;
    width: 1084px;
    height: 1084px;
    background: var(--sign-white);
  }
  .warning-banner {
    position: absolute;
    left: 34px;
    top: 25px;
    width: 1016px;
    height: 230px;
    background: var(--sign-black);
    border-radius: 22px;
    display: flex;
    align-items: center;
    justify-content: center;
    overflow: hidden;
  }
  .warning-title {
    margin: 0;
    color: var(--sign-white);
    font-family: "Saira Stencil One", "Arial Black", sans-serif;
    font-size: 158px;
    line-height: 1;
    letter-spacing: 2px;
    font-weight: 400;
    white-space: nowrap;
    transform: scaleY(1.45);
  }
  .warning-message {
    position: absolute;
    left: 0;
    top: 272px;
    width: 100%;
    margin: 0;
    text-align: center;
    color: var(--sign-black);
    font-weight: 900;
    font-size: 112px;
    line-height: 110px;
    letter-spacing: 2px;
    white-space: nowrap;
  }
  .contact-bar {
    position: absolute;
    left: 34px;
    top: 868px;
    width: 1016px;
    height: 142px;
    background: var(--sign-black);
    border-radius: 22px;
  }
  .company-mark {
    position: absolute;
    left: 60px;
    top: 36px;
    display: flex;
    align-items: center;
    gap: 14px;
  }
  .company-mark-dot {
    width: 64px;
    height: 64px;
    border-radius: 50%;
    background: var(--sign-orange);
  }
  .company-mark-name {
    color: var(--sign-white);
    font-weight: 700;
    font-size: 78px;
    line-height: 1;
  }
  .company-name {
    position: absolute;
    right: 40px;
    top: 10px;
    margin: 0;
    color: var(--sign-orange);
    font-weight: 700;
    font-size: 33px;
    letter-spacing: 3px;
    line-height: 1;
    white-space: nowrap;
  }
  .company-phone {
    position: absolute;
    right: 40px;
    top: 46px;
    margin: 0;
    color: var(--sign-white);
    font-weight: 700;
    font-size: 90px;
    letter-spacing: 3px;
    line-height: 1;
    white-space: nowrap;
  }
  .company-web {
    position: absolute;
    left: 0;
    top: 1030px;
    width: 100%;
    margin: 0;
    text-align: center;
    color: var(--sign-black);
    font-family: "Arial", "Helvetica", sans-serif;
    font-weight: 700;
    font-size: 29px;
    line-height: 1;
  }
</style>
</head>
<body>
  <div class="sign">
    <span class="mount-hole tl"></span>
    <span class="mount-hole tr"></span>
    <span class="mount-hole bl"></span>
    <span class="mount-hole br"></span>

    <div class="sign-face">
      <div class="warning-banner">
        <h1 class="warning-title">WARNING</h1>
      </div>

      <p class="warning-message">ELECTRONIC<br>SURVEILLANCE<br>AND RECORDING<br>DEVICE INSTALLED<br>IN THIS AREA</p>

      <div class="contact-bar">
        <div class="company-mark">
          <span class="company-mark-dot"></span>
          <span class="company-mark-name">HGS</span>
        </div>
        <p class="company-name">HALVORNGATE SECURITY</p>
        <p class="company-phone">1300 418 275</p>
      </div>

      <p class="company-web">www.halvorngate.com.au</p>
    </div>
  </div>
</body>
</html>
```